Plum Meadow Label

Design a label for new brand called Plum Meadow. The specific product label :
Plum Meadow Cocoa Butter Lotion. You only need to design the front label.
I have included the logo and a bottle jpeg with 2 bottles on it. Please try your best.

Industry/Entity Type

Product

Requirements
Must have
• text on the label other than the logo:
cocoa butter
lotion
8.5oz/250ml

Original Moisturizing Formula
Smoothes Marks
Protect Skin

__________________________________
- ALTERNATIVE TEXT TO ALSO USE:
Smoothes Dry Skin, Blemishes & Stretch Marks
Softens Hands, Face and Body
Vitamin E

```html
<!DOCTYPE html>
<html lang="en">
<head>
<meta charset="utf-8">
<title>Plum Meadow Label – Cocoa Butter Lotion</title>
<link rel="stylesheet" href="https://fonts.googleapis.com/css2?family=Montserrat:wght@500;600&family=Alegreya+Sans:wght@400;500&display=swap">
<style>
  :root {
    --cocoa: #7f5142;
    --cocoa-deep: #6f4536;
    --cocoa-soft: #a07a6a;
    --cream: #f4ece6;
    --paper: #ffffff;
    --paper-edge: #ececec;
    --pod-light: #efe6e0;
  }
  html, body {
    margin: 0;
    padding: 0;
    overflow: hidden;
  }
  h1, h2, p {
    margin: 0;
    font-weight: inherit;
  }
  .canvas {
    position: relative;
    width: 1200px;
    height: 1000px;
    background: var(--paper);
    overflow: hidden;
  }

  /* ---------- Dark label ---------- */
  .label-dark {
    position: absolute;
    left: 242px;
    top: 357px;
    width: 294px;
    height: 512px;
  }
  .label-dark .label-shape {
    position: absolute;
    inset: 0;
  }
  .label-dark .content {
    position: absolute;
    inset: 0;
    text-align: center;
    color: var(--cream);
  }
  .label-dark .brand {
    position: absolute;
    top: 88px;
    left: 0;
    right: 0;
    font-family: "Montserrat", sans-serif;
    font-weight: 500;
    font-size: 30px;
    letter-spacing: 0.5px;
    color: var(--cream);
  }
  .label-dark .emblem {
    position: absolute;
    top: 152px;
    left: 90px;
    width: 116px;
    height: 64px;
    border-radius: 50%;
    background: radial-gradient(ellipse at center, #a48474 0%, #8c6252 70%, var(--cocoa) 100%);
  }
  .label-dark .product-name {
    position: absolute;
    top: 238px;
    left: 0;
    right: 0;
    font-family: "Montserrat", sans-serif;
    font-weight: 500;
    color: var(--paper);
  }
  .label-dark .product-name .line-1 {
    display: block;
    font-size: 19px;
    line-height: 23px;
    letter-spacing: 0.4px;
  }
  .label-dark .product-name .line-2 {
    display: block;
    font-size: 17px;
    line-height: 22px;
    letter-spacing: 0.4px;
    margin-top: 1px;
  }
  .label-dark .rule {
    position: absolute;
    top: 296px;
    left: 58px;
    width: 180px;
    height: 1px;
    background: var(--cream);
  }
  .label-dark .claims {
    position: absolute;
    top: 313px;
    left: 0;
    right: 0;
    font-family: "Alegreya Sans", sans-serif;
    font-size: 14px;
    line-height: 16px;
    color: var(--paper);
  }
  .label-dark .volume {
    position: absolute;
    top: 436px;
    left: 0;
    right: 0;
    font-family: "Alegreya Sans", sans-serif;
    font-size: 14px;
    color: var(--paper);
  }

  /* ---------- Light label ---------- */
  .label-light {
    position: absolute;
    left: 660px;
    top: 420px;
    width: 344px;
    height: 450px;
    border: 1px solid var(--paper-edge);
    border-radius: 60px;
    background: var(--paper);
  }
  .label-light .brand {
    position: absolute;
    top: 76px;
    left: 0;
    right: 0;
    text-align: center;
    font-family: "Montserrat", sans-serif;
    font-weight: 500;
    font-size: 32px;
    letter-spacing: 0.5px;
    color: var(--cocoa);
  }
  .label-light .product-name {
    position: absolute;
    top: 188px;
    left: 22px;
    font-family: "Montserrat", sans-serif;
    font-weight: 500;
    font-size: 19px;
    line-height: 27px;
    letter-spacing: 1px;
    color: var(--cocoa);
  }
  .label-light .divider {
    position: absolute;
    top: 188px;
    left: 141px;
    width: 1px;
    height: 77px;
    background: var(--cocoa);
  }
  .label-light .pod-art {
    position: absolute;
    top: 188px;
    left: 154px;
    width: 122px;
    height: 80px;
    border-radius: 50% 50% 45% 45%;
    background: radial-gradient(ellipse at center, #d9c6bc 0%, var(--pod-light) 75%, var(--paper) 100%);
  }
  .label-light .rule {
    position: absolute;
    top: 273px;
    left: 26px;
    width: 248px;
    height: 1px;
    background: var(--cocoa);
  }
  .label-light .claims {
    position: absolute;
    top: 283px;
    left: 26px;
    width: 250px;
    font-family: "Alegreya Sans", sans-serif;
    font-size: 14px;
    line-height: 17px;
    color: var(--cocoa);
  }
  .label-light .volume {
    position: absolute;
    top: 364px;
    left: 169px;
    width: 105px;
    height: 23px;
    line-height: 23px;
    text-align: center;
    background: var(--cocoa);
    font-family: "Alegreya Sans", sans-serif;
    font-size: 14px;
    color: var(--paper);
  }
</style>
</head>
<body>
<main class="canvas">

  <section class="label-dark" aria-label="Plum Meadow Cocoa Butter Lotion label, dark version">
    <svg class="label-shape" width="294" height="512" viewBox="0 0 294 512" aria-hidden="true">
      <path d="M42,0 H252 Q294,0 294,64 V448 Q294,512 232,512 H62 Q0,512 0,448 V64 Q0,0 42,0 Z" fill="var(--cocoa)"/>
    </svg>
    <div class="content">
      <div class="brand">Plum Meadow</div>
      <div class="emblem" role="img" aria-label="Engraved cocoa pod with leaves inside an oval emblem"></div>
      <h1 class="product-name">
        <span class="line-1">COCOA BUTTER ™</span>
        <span class="line-2">LOTION</span>
      </h1>
      <div class="rule"></div>
      <p class="claims">
        Smoothes Dry Skin,<br>
        Blemishes &amp; Stretch Marks<br>
        Softens Hands, Face and Body<br>
        Vitamin E
      </p>
      <div class="volume">8.5oz | 250ml</div>
    </div>
  </section>

  <section class="label-light" aria-label="Plum Meadow Cocoa Butter Lotion label, light version">
    <div class="brand">Plum Meadow</div>
    <h2 class="product-name">COCOA<br>BUTTER<br>LOTION ™</h2>
    <div class="divider"></div>
    <div class="pod-art" role="img" aria-label="Engraved cocoa pod with leaves illustration"></div>
    <div class="rule"></div>
    <p class="claims">
      Smoothes Dry Skin, Blemishes &amp; Stretch Marks Softens Hands, Face and Body<br>
      Vitamin E
    </p>
    <div class="volume">8.5oz | 250ml</div>
  </section>

</main>
</body>
</html>
```